Business Card Design

We need elegant business card design. We are conglomerate for different businesses. Nature of our businesses include Construction, Health care, Energy and Automotive

Target Market(s)

Business to business clients ages 40+

Industry/Entity Type

Automotive

Contact Information for Business Card

Darian (Dax) Kellum
CEO
Brightpath Group of Companies, Inc
3917 Larkmoor Rd E, Houston, TX, 77431
C:832-406-1357 O: 281-739-4016 F: 281-612-9548

```html
<!DOCTYPE html>
<html lang="en">
<head>
<meta charset="utf-8">
<title>Brightpath Group of Companies – Business Card</title>
<link rel="stylesheet" href="https://fonts.googleapis.com/css2?family=Oxanium:wght@500&display=swap">
<style>
  :root {
    --backdrop: #1c1c1c;
    --card: #f7f7f5;
    --ink: #2a2a2a;
  }
  * { box-sizing: border-box; margin: 0; padding: 0; }
  html, body {
    width: 1200px;
    height: 758px;
    overflow: hidden;
    background: var(--backdrop);
  }
  .card {
    position: absolute;
    left: 90px;
    top: 80px;
    width: 1020px;
    height: 598px;
    background: var(--card);
    color: var(--ink);
    font-family: "Oxanium", sans-serif;
    font-weight: 500;
    text-transform: uppercase;
  }
  .brand {
    position: absolute;
    left: 0;
    right: 0;
    top: 120px;
    display: flex;
    flex-direction: column;
    align-items: center;
    gap: 14px;
  }
  .brand__mark {
    width: 22px;
    height: 22px;
    border: 3px solid var(--ink);
    border-radius: 50%;
  }
  .brand__name {
    font-size: 46px;
    letter-spacing: 4px;
    line-height: 1;
  }
  .brand__tagline {
    font-size: 20px;
    letter-spacing: 2px;
    line-height: 1;
  }
  .holder {
    position: absolute;
    left: 0;
    right: 0;
    top: 330px;
    text-align: center;
  }
  .holder__name {
    display: inline-block;
    font-size: 25px;
    letter-spacing: 1.5px;
    padding: 0 40px 8px;
    border-bottom: 3px solid var(--ink);
  }
  .contacts {
    position: absolute;
    left: 70px;
    right: 70px;
    top: 400px;
    font-size: 25px;
    letter-spacing: 1px;
  }
  .contacts__row {
    display: flex;
    align-items: center;
    gap: 44px;
    margin-bottom: 26px;
  }
  .contacts__row--address { justify-content: flex-end; }
  .contacts__row--phones { justify-content: flex-start; }
  .contact {
    display: flex;
    align-items: center;
    gap: 12px;
    white-space: nowrap;
  }
  .contact svg { fill: var(--ink); flex: none; }
</style>
</head>
<body>
  <div class="card">
    <div class="brand">
      <span class="brand__mark" aria-hidden="true"></span>
      <div class="brand__name">Brightpath</div>
      <div class="brand__tagline">Group of Companies, Inc</div>
    </div>

    <div class="holder">
      <span class="holder__name">Darian (Dax) Kellum</span>
    </div>

    <div class="contacts">
      <div class="contacts__row contacts__row--address">
        <span class="contact contact--address">3917 Larkmoor Rd E, Houston, TX, 77431</span>
        <span class="contact contact--fax">
          <svg width="38" height="28" viewBox="0 0 38 28" aria-label="Fax">
            <rect x="9" y="0" width="20" height="8"/>
            <rect x="0" y="9" width="38" height="13" rx="2"/>
            <rect x="7" y="18" width="24" height="10" fill="#f7f7f5"/>
            <rect x="9" y="20" width="20" height="8"/>
          </svg>
          281-612-9548
        </span>
      </div>
      <div class="contacts__row contacts__row--phones">
        <span class="contact contact--mobile">
          <svg width="16" height="26" viewBox="0 0 16 26" aria-label="Mobile">
            <path d="M3 0h10a3 3 0 0 1 3 3v20a3 3 0 0 1-3 3H3a3 3 0 0 1-3-3V3a3 3 0 0 1 3-3zm0 4v16h10V4z"/>
          </svg>
          832-406-1357
        </span>
        <span class="contact contact--office">
          <svg width="26" height="26" viewBox="0 0 24 24" aria-label="Office phone">
            <path d="M6.6 10.8a15.1 15.1 0 0 0 6.6 6.6l2.2-2.2a1 1 0 0 1 1-.25 11.4 11.4 0 0 0 3.6.57 1 1 0 0 1 1 1V20a1 1 0 0 1-1 1A17 17 0 0 1 3 4a1 1 0 0 1 1-1h3.5a1 1 0 0 1 1 1c0 1.25.2 2.45.57 3.57a1 1 0 0 1-.25 1z"/>
          </svg>
          281-739-4016
        </span>
      </div>
    </div>
  </div>
</body>
</html>
```